Brindle Capital and Investments

Create a simple business card design using the logos attached. Make it similar but not exact to the reference photo. Brand guidelines are also included.

```html
<!DOCTYPE html>
<html lang="en">
<head>
<meta charset="utf-8">
<title>Brindle Capital – Business Card</title>
<link rel="stylesheet" href="https://fonts.googleapis.com/css2?family=Montserrat:wght@400;500;700;800&display=swap">
<style>
  :root {
    --backdrop: #2f2f31;
    --card-white: #ffffff;
    --copper: #a8501f;
    --copper-light: #c9703a;
    --copper-dark: #8a3f17;
    --navy: #1f2940;
    --ink: #1c1c1c;
  }
  * { margin: 0; padding: 0; box-sizing: border-box; }
  html, body {
    width: 1200px; height: 875px; overflow: hidden;
    background: var(--backdrop);
    font-family: "Montserrat", sans-serif;
  }
  .canvas { position: relative; width: 1200px; height: 875px; }

  .card {
    position: absolute;
    width: 580px; height: 332px;
    border-radius: 20px;
  }
  .card-front {
    left: 80px; top: 110px;
    background: var(--card-white);
    display: flex; align-items: center;
  }
  .card-back {
    left: 540px; top: 445px;
    background: linear-gradient(135deg, var(--copper-dark) 0%, var(--copper) 55%, var(--copper-light) 100%);
  }

  .brand-block {
    width: 270px; height: 100%;
    display: flex; flex-direction: column; align-items: center; justify-content: center; gap: 14px;
  }
  .brand-dot {
    width: 34px; height: 34px; border-radius: 50%;
    background: var(--copper);
  }
  .brand-name {
    font-weight: 800; font-size: 30px; letter-spacing: 3px;
    color: var(--navy); text-transform: uppercase; text-align: center; line-height: 1.15;
  }

  .divider {
    width: 1.5px; height: 200px; background: var(--copper);
  }

  .contact-block { padding-left: 34px; color: var(--ink); }
  .person-name {
    font-weight: 800; font-size: 24px; color: var(--copper);
    text-transform: uppercase; letter-spacing: 0.5px;
  }
  .person-title { font-size: 14px; margin-top: 2px; }
  .address { font-size: 14px; line-height: 1.45; margin-top: 18px; }
  .contact-list { list-style: none; margin-top: 14px; font-size: 14px; line-height: 1.6; }
  .contact-list li { display: flex; align-items: center; gap: 9px; }
  .contact-list svg { width: 13px; height: 13px; fill: var(--copper); flex: none; }
</style>
</head>
<body>
<main class="canvas">
  <section class="card card-front" aria-label="Business card front">
    <div class="brand-block">
      <span class="brand-dot"></span>
      <p class="brand-name">Brindle<br>Capital</p>
    </div>
    <span class="divider"></span>
    <div class="contact-block">
      <h1 class="person-name">Maren Tolliver</h1>
      <p class="person-title">Managing Director</p>
      <p class="address">Your address, City<br>State, Zip 1200</p>
      <ul class="contact-list">
        <li>
          <svg viewBox="0 0 16 16" aria-hidden="true"><path d="M3.5 1.5l2.5 0 1 3.5-1.6 1.2a8 8 0 0 0 4.4 4.4l1.2-1.6 3.5 1v2.5c0 .8-.7 1.5-1.5 1.5A12.5 12.5 0 0 1 2 3c0-.8.7-1.5 1.5-1.5z"/></svg>
          123 456 700
        </li>
        <li>
          <svg viewBox="0 0 16 16" aria-hidden="true"><path d="M4.5 1h7a1 1 0 0 1 1 1v12a1 1 0 0 1-1 1h-7a1 1 0 0 1-1-1V2a1 1 0 0 1 1-1zm1 1.5v9.5h5V2.5zM8 12.7a.8.8 0 1 0 0 1.6.8.8 0 0 0 0-1.6z"/></svg>
          123 456 700
        </li>
        <li>
          <svg viewBox="0 0 16 16" aria-hidden="true"><path d="M1 3h14v10H1zm1.6 1.3L8 8.6l5.4-4.3z"/></svg>
          info@brindlecapital.com
        </li>
        <li>
          <svg viewBox="0 0 16 16" aria-hidden="true"><path d="M8 1a7 7 0 1 0 0 14A7 7 0 0 0 8 1zm0 1.5c.7 0 1.6 1.6 1.9 4.5H6.1C6.4 4.1 7.3 2.5 8 2.5zM2.6 9h2.1c.1 1.5.4 2.8.9 3.8A5.5 5.5 0 0 1 2.6 9zm0-2a5.5 5.5 0 0 1 3-3.8c-.5 1-.8 2.3-.9 3.8zm5.4 6.5c-.7 0-1.6-1.6-1.9-4.5h3.8c-.3 2.9-1.2 4.5-1.9 4.5zm2.4-.7c.5-1 .8-2.3.9-3.8h2.1a5.5 5.5 0 0 1-3 3.8zM11.3 7c-.1-1.5-.4-2.8-.9-3.8a5.5 5.5 0 0 1 3 3.8z"/></svg>
          www.brindlecapital.com
        </li>
      </ul>
    </div>
  </section>

  <section class="card card-back" role="img" aria-label="Card back: repeating embossed brand-mark pattern on glossy copper"></section>
</main>
</body>
</html>
```